I need a book cover for a 6x9 book. The front cover information (title and author) is below, and the back cover information will be given to the winning designer. I am wanting something vibrant and bright, and I am open to your creativity, but I do not want any pictures of people on the cover. Save room for the barcode on the back cover.
Title:
Oops! Wrong Turn?
Quiet Rooms Explained: Notes on Patient Gardening Habits
Author:
Marisol Tembe

```html
<!DOCTYPE html>
<html lang="en">
<head>
<meta charset="utf-8">
<title>Oops! Wrong Turn? — Book Cover</title>
<link rel="stylesheet" href="https://fonts.googleapis.com/css2?family=Anton&family=Quicksand:wght@700&display=swap">
<style>
  :root {
    --stage: #e4e8ec;
    --paper: #ffffff;
    --magenta: #f2036f;
    --rose: #e5306a;
    --ink: #0b0b0b;
    --sun: #ffe81a;
    --art-top: #f4f2f5;
    --art-warm: #d9b8a8;
    --art-mid: #b58aa6;
    --art-cool: #8fa6b8;
  }
  * { box-sizing: border-box; margin: 0; padding: 0; }
  html, body { width: 1200px; height: 871px; overflow: hidden; background: var(--stage); }
  .cover {
    position: absolute; left: 333px; top: 35px;
    width: 534px; height: 800px;
    background: var(--paper);
    overflow: hidden;
    box-shadow: 0 10px 30px rgba(0,0,0,.12);
  }
  .title-bubble { position: absolute; left: 196px; top: 48px; width: 310px; height: 130px; }
  .title-bubble svg { position: absolute; inset: 0; }
  .title-bubble span {
    position: absolute; left: 30px; top: 0; width: 280px; height: 118px;
    display: flex; align-items: center; justify-content: center;
    font-family: "Quicksand", sans-serif; font-weight: 700;
    font-size: 88px; line-height: 1; color: var(--paper); letter-spacing: -1px;
  }
  .title-main {
    position: absolute; left: 0; right: 24px; top: 174px;
    text-align: right; white-space: nowrap;
    font-family: "Anton", sans-serif; font-weight: 400;
    font-size: 86px; line-height: 1;
    color: var(--ink); letter-spacing: 1px;
  }
  .subtitle-band {
    position: absolute; left: 0; top: 294px; width: 490px; height: 58px;
    background: linear-gradient(90deg, var(--magenta) 0%, var(--magenta) 42%, rgba(242,3,111,0.35) 75%, rgba(242,3,111,0) 100%);
  }
  .subtitle {
    position: absolute; left: 22px; top: 299px;
    font-family: "Quicksand", sans-serif; font-weight: 700;
    font-size: 19px; line-height: 1.28; color: var(--sun);
    white-space: nowrap;
  }
  .illustration {
    position: absolute; left: 24px; top: 372px; width: 486px; height: 330px;
    border-radius: 24px 24px 0 0;
    background:
      linear-gradient(180deg, var(--art-top) 0%, rgba(244,242,245,0) 45%),
      linear-gradient(90deg, var(--art-warm) 0%, var(--art-mid) 50%, var(--art-cool) 100%);
  }
  .author-band {
    position: absolute; left: 0; bottom: 0; width: 534px; height: 100px;
    background: var(--magenta);
    display: flex; align-items: center; justify-content: center;
  }
  .author {
    font-family: "Quicksand", sans-serif; font-weight: 700;
    font-size: 40px; line-height: 1; color: var(--paper); letter-spacing: 3px;
  }
</style>
</head>
<body>
  <main class="cover">
    <div class="title-bubble">
      <svg viewBox="0 0 310 130" width="310" height="130" aria-hidden="true">
        <path d="M52 0 H288 Q310 0 310 22 V96 Q310 118 288 118 H40 Q30 118 26 110 L0 124 L20 100 Q30 94 30 80 V22 Q30 0 52 0 Z" fill="var(--rose)"/>
      </svg>
      <span>Oops!</span>
    </div>
    <h1 class="title-main">WRONG TURN?</h1>

    <div class="subtitle-band"></div>
    <p class="subtitle">Quiet Rooms Explained:<br>Notes on Patient Gardening Habits</p>

    <div class="illustration" role="img" aria-label="Illustration of three friends waving, each with a colourful speech bubble of greetings above them"></div>

    <footer class="author-band">
      <p class="author">Marisol Tembe</p>
    </footer>
  </main>
</body>
</html>
```